Tallyleaf Web Design

Create Website Design for Tallyleaf. Tallyleaf is online application for collaboration team work system (task list management). More concept design for this project please find attach file ("tallyleaf website concept.pdf") . But my concept is just describe minimal features not bind design

For tallyleaf logo, i had already attach files. But i had not decided what color i chose, so it's okay if you suggest logo color for your suitable website design.
Updates

Dear All Designer,

I like brisk carousel (http://quorvanlabs.example/brisk-carousel/),
may be your concept design can adjust with this concept.
but don't worry about script for brisk carousel, my team will be handle
You just make website design to suitable with brisk carousel

but if you had own website design concept are welcome

thanks

Target Market(s)

Business Company

Industry/Entity Type

Management

```html
<!DOCTYPE html>
<html lang="en">
<head>
<meta charset="utf-8">
<title>Tallyleaf</title>
<link href="https://fonts.googleapis.com/css2?family=Arimo:wght@400;700&family=Lato:wght@400;700&display=swap" rel="stylesheet">
<style>
:root{
  --page-bg:#efefef;
  --white:#ffffff;
  --nav-text:#555555;
  --brand-blue:#2a78b0;
  --brand-teal:#2fa5c8;
  --hero-top:#6fc3dd;
  --hero-mid:#2fa0c6;
  --hero-deep:#1a86b3;
  --orange:#f07a14;
  --orange-light:#fba23a;
  --card-border:#e2e2e2;
  --body-text:#666666;
  --footer-bg:#3d3d3d;
  --footer-bar:#2e2e2e;
  --footer-head:#eeeeee;
  --footer-link:#cfcfcf;
  --footer-rule:#555555;
}
*{box-sizing:border-box;margin:0;padding:0}
html,body{width:1200px;height:1200px;overflow:hidden}
body{background:var(--page-bg);font-family:'Arimo',Arial,sans-serif;position:relative}
.abs{position:absolute}

.site-header{left:0;top:0;width:1200px;height:78px;background:linear-gradient(#fff,#f6f6f6);border-bottom:1px solid #dcdcdc}
.brand{left:110px;top:22px;display:flex;align-items:center;gap:10px}
.brand-name{font-size:40px;color:var(--brand-teal);font-weight:400;letter-spacing:-1px}
.brand-dot{width:22px;height:22px;border-radius:50%;background:var(--brand-teal)}
.main-nav{left:541px;top:36px;display:flex;font-size:13px;color:var(--nav-text)}
.main-nav span{padding:0 8px;border-right:1px dotted #999;line-height:16px}
.main-nav span:last-child{border-right:none}
.btn-login,.btn-signup{top:30px;height:28px;width:71px;font-size:13px;font-weight:700;text-align:center;line-height:26px}
.btn-login{left:949px;background:linear-gradient(#f4f4f4,#d9d9d9);border:1px solid #b8b8b8;color:#555}
.btn-signup{left:1026px;background:linear-gradient(#5cc7e6,#2a9fcc);border:1px solid #2189b3;color:#fff}

.hero{left:0;top:79px;width:1200px;height:356px;background:radial-gradient(ellipse at 70% 20%,var(--hero-top),var(--hero-mid) 55%,var(--hero-deep))}
.hero-shadow{left:110px;top:435px;width:980px;height:40px;background:radial-gradient(ellipse at 50% 0%,rgba(0,0,0,.22),rgba(0,0,0,0) 70%)}
.hero-visual{left:118px;top:115px;width:520px;height:320px;border-radius:18px 18px 0 0;background:linear-gradient(#2c3d55,#5b7590 60%,#dfe6ec)}
.hero-title{left:660px;top:136px;width:424px;text-align:center;color:#fff;font-size:46px;font-weight:700;line-height:55px;text-shadow:0 2px 3px rgba(0,0,0,.35)}
.cta{left:757px;top:329px;width:258px;height:50px;border-radius:3px;background:linear-gradient(var(--orange-light),var(--orange));color:#fff;font-size:23px;font-weight:700;text-align:center;line-height:50px;box-shadow:0 2px 3px rgba(0,0,0,.3)}
.cta-notch{left:876px;top:318px}

.card{top:520px;width:312px;height:311px;background:#fff;border:1px solid var(--card-border)}
.card-title{position:absolute;left:16px;right:16px;top:28px;text-align:center;font-size:19px;font-weight:700;color:var(--brand-blue);padding-bottom:6px;border-bottom:1px dashed #cccccc}
.card-visual{position:absolute;left:40px;right:40px;top:64px;height:156px;border-radius:6px}
.card-text{position:absolute;left:10px;right:10px;top:226px;text-align:center;font-family:'Lato',Arial,sans-serif;font-size:14px;line-height:18px;color:var(--body-text)}
.read-more{position:absolute;left:0;right:0;top:270px;text-align:center;font-size:10px;font-weight:700;color:var(--brand-blue)}

.footer{left:0;top:903px;width:1200px;height:240px;background:var(--footer-bg)}
.footer-bar{left:0;top:1143px;width:1200px;height:45px;background:var(--footer-bar);color:#888;font-size:11px;text-align:center;line-height:45px}
.col-head{top:936px;font-size:17px;color:var(--footer-head)}
.link-list{top:962px;width:190px;list-style:none}
.link-list li{height:33px;line-height:32px;font-size:13px;color:var(--footer-link);border-bottom:1px solid var(--footer-rule)}
.link-list li:last-child{border-bottom:none}
.social-list{left:624px;top:962px;width:190px;list-style:none}
.social-list li{height:33px;line-height:32px;font-size:13px;color:var(--footer-link);border-bottom:1px solid var(--footer-rule);display:flex;align-items:center;gap:17px;padding-left:6px}
.social-list li:last-child{border-bottom:none}
.social-mark{width:20px;height:20px;border-radius:3px}
.field{background:#fff;border:1px solid #ccc;font-size:13px;color:#888;padding:0 10px;line-height:32px}
.submit{left:840px;top:1087px;width:115px;height:28px;background:linear-gradient(var(--orange-light),var(--orange));border:1px solid #c75f08;color:#fff;font-size:14px;font-weight:700;text-align:center;line-height:26px}
</style>
</head>
<body>
<header class="site-header abs">
  <div class="brand abs"><span class="brand-name">tallyleaf</span><span class="brand-dot"></span></div>
  <nav class="main-nav abs"><span>Home</span><span>Pricing</span><span>Features</span><span>Support</span><span>About us</span><span>Contact us</span></nav>
  <div class="btn-login abs">LOGIN</div>
  <div class="btn-signup abs">SIGNUP</div>
</header>

<section class="hero abs"></section>
<div class="hero-shadow abs"></div>
<div class="hero-visual abs" role="img" aria-label="Laptop showing the Tallyleaf dashboard with a video play button"></div>
<h1 class="hero-title abs">Customize Online Collaboration Team Work</h1>
<svg class="cta-notch abs" width="18" height="12" viewBox="0 0 18 12"><polygon points="0,12 9,0 18,12" fill="#fba23a"/></svg>
<div class="cta abs">Get Started Now</div>

<article class="card abs" style="left:108px">
  <h2 class="card-title">CUSTOMIZE APPLICATION</h2>
  <div class="card-visual" role="img" aria-label="Open box filled with colourful app tiles" style="background:radial-gradient(circle,#e4eef6,#ffffff 70%)"></div>
  <p class="card-text">Lorem ipsum dolor sit amet. Sed do eiusmod tempor incididunt ut labor</p>
  <div class="read-more">READ MORE &nbsp;»</div>
</article>
<article class="card abs" style="left:448px">
  <h2 class="card-title">SYNCHRONIZE ALL DEVICE</h2>
  <div class="card-visual" role="img" aria-label="Cloud connected to laptop, phone and tablet" style="background:radial-gradient(circle,#dbeefb,#ffffff 70%)"></div>
  <p class="card-text">Lorem ipsum dolor sit amet. Sed do eiusmod tempor incididunt ut labor</p>
  <div class="read-more">READ MORE &nbsp;»</div>
</article>
<article class="card abs" style="left:783px">
  <h2 class="card-title">REPORT</h2>
  <div class="card-visual" role="img" aria-label="Laptop showing bar and pie chart reports" style="background:radial-gradient(circle,#e8eef4,#ffffff 70%)"></div>
  <p class="card-text">Lorem ipsum dolor sit amet. Sed do eiusmod tempor incididunt ut labor</p>
  <div class="read-more">READ MORE &nbsp;»</div>
</article>

<footer class="footer abs"></footer>
<h3 class="col-head abs" style="left:147px;font-weight:400">Navigations</h3>
<h3 class="col-head abs" style="left:389px;font-weight:400">Links</h3>
<h3 class="col-head abs" style="left:624px;font-weight:400">Social</h3>
<h3 class="col-head abs" style="left:839px;font-weight:400">Contact Us</h3>
<ul class="link-list abs" style="left:135px;padding-left:12px"><li>Home</li><li>Pricing</li><li>Features</li><li>Support</li><li>Contact Us</li></ul>
<ul class="link-list abs" style="left:389px"><li>FAQ</li><li>Terms &amp; Conditions</li><li>Privacy Policy</li><li>Customers</li><li>Disclamer</li></ul>
<ul class="social-list abs">
  <li><span class="social-mark" style="background:#3b5b98"></span>Friendloop</li>
  <li><span class="social-mark" style="background:#33b5e5"></span>Chirpwire</li>
  <li><span class="social-mark" style="background:#222"></span>Searchly</li>
  <li><span class="social-mark" style="background:#f26b1d"></span>RSS</li>
</ul>
<div class="field abs" style="left:839px;top:976px;width:110px;height:33px">Your Name</div>
<div class="field abs" style="left:959px;top:976px;width:110px;height:33px">Your email</div>
<div class="field abs" style="left:839px;top:1018px;width:230px;height:58px">Enter your Message</div>
<div class="submit abs">SUBMIT NOW!</div>
<div class="footer-bar abs">Copyright © 2013 tallyleaf.example All rights reserved.</div>
</body>
</html>
```